Shine Crew

I need a flyer and business cards to hand out at office buildings and country clubs introducing my new auto detailing business, SHINE CREW. Call or text 913-555-0147 for an appointment. Complete auto detailing done at their place or mine, and we offer pick -up and drop-off, if needed. I believe the flyer needs a car on it. Black, blue, and pink are my preferred colors. While you go about your day's business, whether playing 18 holes of golf or putting in 8 hours at the office, we will have your ride shining like a new penny when you're ready to roll!

```html
<!DOCTYPE html>
<html lang="en">
<head>
<meta charset="utf-8">
<title>Shine Crew – Flyer &amp; Business Card</title>
<link href="https://fonts.googleapis.com/css2?family=Montserrat:wght@500;600;700;800;900&family=Roboto+Condensed:wght@500;700&display=swap" rel="stylesheet">
<style>
  :root{
    --board:#939393;
    --navy:#0d0b3f;
    --indigo:#2a1166;
    --violet:#6a2596;
    --magenta:#a8449c;
    --gold-light:#fbd54a;
    --gold:#f3b22a;
    --orange:#e8922a;
    --ink:#0f1a2e;
    --white:#ffffff;
    --lavender:#b86bd1;
  }
  *{margin:0;padding:0;box-sizing:border-box}
  html,body{width:1200px;height:2886px;overflow:hidden;background:var(--board)}
  body{position:relative;font-family:"Montserrat",sans-serif;color:var(--white)}

  .flyer{position:absolute;left:120px;top:90px;width:960px;height:1334px;overflow:hidden;
    background:
      radial-gradient(circle at 85% 14%, rgba(90,110,255,.35) 0, transparent 22%),
      radial-gradient(circle at 12% 30%, rgba(90,110,255,.25) 0, transparent 18%),
      linear-gradient(180deg,var(--navy) 0%,var(--indigo) 32%,var(--violet) 62%,var(--magenta) 100%);
    box-shadow:-30px 30px 40px rgba(0,0,0,.35)}
  .gold-text{background:linear-gradient(180deg,var(--gold-light) 0%,var(--gold) 55%,var(--orange) 100%);
    -webkit-background-clip:text;background-clip:text;color:transparent}
  .abs{position:absolute}

  .flyer .brand-main{left:0;width:100%;top:86px;text-align:center;font-weight:900;font-size:198px;line-height:1;letter-spacing:-2px}
  .flyer .brand-sub{left:0;width:100%;top:262px;text-align:center;font-weight:600;font-size:104px;line-height:1;letter-spacing:2px}
  .flyer .tagline{left:0;width:100%;top:374px;text-align:center;font-weight:600;font-size:31px;line-height:37px}

  .offer{left:592px;top:477px;width:286px;height:216px;border-radius:40px 40px 0 0;z-index:2;
    background:linear-gradient(180deg,var(--orange) 0%,var(--gold) 100%);border:3px solid var(--magenta);
    text-align:center;color:var(--ink);padding-top:18px}
  .offer .head{font-weight:800;font-size:32px;line-height:34px}
  .offer .body{font-weight:800;font-size:26px;line-height:27px;color:var(--white)}
  .offer .note{font-weight:600;font-size:17px;line-height:20px}

  .car-photo{z-index:1;left:71px;top:620px;width:816px;height:290px;border-radius:40% 30% 10% 12% / 60% 50% 20% 20%;
    background:radial-gradient(ellipse at 55% 45%,#3a3a44 0%,#141418 55%,#050507 100%)}

  .service-photo{left:83px;width:268px;height:162px;border:6px solid var(--white);border-radius:16px}
  .service-photo.interior{top:918px;background:linear-gradient(135deg,#4a4a4f,#1b1b1f)}
  .service-photo.polish{top:1090px;background:linear-gradient(135deg,#1b2a6b,#2f4fa8 55%,#0f1430)}

  .benefits{left:402px;top:940px;list-style:none;font-weight:500;font-size:22px;line-height:37px}
  .benefits li{display:flex;align-items:center;gap:16px}
  .benefits svg{width:22px;height:22px}

  .promise{left:402px;top:1057px;width:558px;height:57px;padding:3px 0 0 36px;
    background:linear-gradient(90deg,var(--gold-light) 0%,var(--gold) 100%);
    color:var(--ink);font-weight:600;font-size:21.5px;line-height:24px}

  .call-tag{left:398px;top:1138px;width:362px;height:34px;padding-left:10px;
    border-radius:12px 0 0 0;border-left:3px solid var(--orange);border-bottom:2px solid var(--gold);
    font-family:"Roboto Condensed",sans-serif;font-weight:500;font-size:22px;line-height:32px;color:var(--white);
    background:linear-gradient(90deg,rgba(120,60,20,.6),transparent 80%)}
  .book{left:402px;top:1182px;width:374px;height:36px;border-radius:8px;background:var(--ink);
    font-family:"Roboto Condensed",sans-serif;font-weight:500;font-size:25px;line-height:36px;color:var(--gold-light);text-align:center}
  .phone{left:432px;top:1222px;font-family:"Roboto Condensed",sans-serif;font-weight:500;font-size:37px;line-height:44px;
    display:flex;align-items:center;gap:6px}
  .phone svg{width:26px;height:26px}

  .chevrons{position:absolute}

  .card{position:absolute;left:150px;top:1560px;width:900px;height:514px;overflow:hidden;
    background:
      radial-gradient(circle at 80% 10%, rgba(90,110,255,.3) 0, transparent 25%),
      linear-gradient(180deg,var(--navy) 0%,var(--indigo) 38%,var(--violet) 70%,var(--magenta) 100%);
    box-shadow:-30px 30px 40px rgba(0,0,0,.35)}
  .card .brand-main{left:48px;top:30px;font-weight:900;font-size:112px;line-height:1;letter-spacing:-1px}
  .card .brand-sub-row{left:64px;top:126px;width:350px;display:flex;align-items:center;gap:14px}
  .card .brand-sub-row .rule{flex:1;height:3px;background:var(--gold)}
  .card .brand-sub{font-weight:600;font-size:50px;line-height:56px;letter-spacing:1px}
  .card .tagline{left:62px;top:198px;font-weight:500;font-size:21px}
  .card .person{left:668px;top:62px}
  .card .person .name{font-weight:700;font-size:27px;color:var(--gold)}
  .card .person .role{font-weight:500;font-size:21px;color:#d8c9ef}
  .card .car-photo{left:394px;top:260px;width:540px;height:240px;border-radius:50% 40% 12% 16% / 46% 40% 20% 20%}
  .card .call-tag{left:40px;top:392px;width:262px;height:30px;font-size:18px;line-height:28px}
  .card .phone{left:62px;top:428px;font-size:32px}
  .card .phone svg{width:22px;height:22px}
</style>
</head>
<body>

<section class="flyer">
  <div class="abs brand-main gold-text">SHINE</div>
  <div class="abs brand-sub gold-text">CREW</div>
  <svg class="chevrons" style="left:722px;top:295px" width="94" height="54" viewBox="0 0 94 54">
    <g fill="none" stroke="var(--lavender)" stroke-width="8">
      <polyline points="28,4 8,27 28,50"/><polyline points="50,4 30,27 50,50"/><polyline points="72,4 52,27 72,50"/><polyline points="94,4 74,27 94,50"/>
    </g>
  </svg>
  <p class="abs tagline">Complete Auto Detailing Interior &amp; Exterior<br>done at your place or at our workshop!</p>
  <svg class="chevrons" style="left:85px;top:462px" width="40" height="78" viewBox="0 0 40 78">
    <g fill="none" stroke="var(--lavender)" stroke-width="6">
      <polyline points="2,4 20,18 38,4"/><polyline points="2,22 20,36 38,22"/><polyline points="2,40 20,54 38,40"/><polyline points="2,58 20,72 38,58"/>
    </g>
  </svg>

  <div class="abs offer">
    <div class="head">WE OFFER</div>
    <div class="body">PICK-UP<br>&amp; DROP-OFF<br>SERVICES</div>
    <div class="note">If Needed</div>
  </div>

  <div class="abs car-photo" role="img" aria-label="Glossy black sports sedan, front three-quarter view"></div>

  <div class="abs service-photo interior" role="img" aria-label="Detailer vacuuming a car interior"></div>
  <div class="abs service-photo polish" role="img" aria-label="Detailer polishing the hood of a blue car"></div>

  <ul class="abs benefits">
    <li><svg viewBox="0 0 22 22"><circle cx="11" cy="11" r="9.5" fill="none" stroke="var(--gold)" stroke-width="2"/><polyline points="6.5,11 10,14.5 16,7.5" fill="none" stroke="var(--gold)" stroke-width="2"/></svg>While you go about your day's business</li>
    <li><svg viewBox="0 0 22 22"><circle cx="11" cy="11" r="9.5" fill="none" stroke="var(--gold)" stroke-width="2"/><polyline points="6.5,11 10,14.5 16,7.5" fill="none" stroke="var(--gold)" stroke-width="2"/></svg>Whether playing 18 holes of golf</li>
    <li><svg viewBox="0 0 22 22"><circle cx="11" cy="11" r="9.5" fill="none" stroke="var(--gold)" stroke-width="2"/><polyline points="6.5,11 10,14.5 16,7.5" fill="none" stroke="var(--gold)" stroke-width="2"/></svg>Putting in 8 hours at the office</li>
  </ul>

  <p class="abs promise">We will have your ride shining like a new<br>penny when you're ready to roll!</p>

  <div class="abs call-tag">Call or Text for Appointment</div>
  <div class="abs book">BOOK YOUR SHINE TODAY!</div>
  <div class="abs phone">
    <svg viewBox="0 0 24 24"><path fill="var(--white)" d="M6.6 10.8c1.4 2.8 3.8 5.1 6.6 6.6l2.2-2.2c.3-.3.7-.4 1-.2 1.1.4 2.3.6 3.6.6.6 0 1 .4 1 1V20c0 .6-.4 1-1 1C10.6 21 3 13.4 3 4c0-.6.4-1 1-1h3.5c.6 0 1 .4 1 1 0 1.300.2 2.500.6 3.600.1.3 0 .7-.2 1z"/></svg>
    913-555-0147
  </div>
  <svg class="chevrons" style="left:786px;top:1227px" width="94" height="54" viewBox="0 0 94 54">
    <g fill="none" stroke="var(--lavender)" stroke-width="8">
      <polyline points="28,4 8,27 28,50"/><polyline points="50,4 30,27 50,50"/><polyline points="72,4 52,27 72,50"/><polyline points="94,4 74,27 94,50"/>
    </g>
  </svg>
</section>

<section class="card">
  <div class="abs brand-main gold-text">SHINE</div>
  <div class="abs brand-sub-row"><span class="rule"></span><span class="brand-sub gold-text">CREW</span><span class="rule"></span></div>
  <p class="abs tagline">Auto Detailing Interior &amp; Exterior</p>
  <div class="abs person">
    <div class="name">Alex Rivera</div>
    <div class="role">Auto Detailer</div>
  </div>
  <svg class="chevrons" style="left:800px;top:140px" width="60" height="110" viewBox="0 0 60 110">
    <g fill="none" stroke="var(--lavender)" stroke-width="7">
      <polyline points="4,6 30,24 56,6"/><polyline points="4,32 30,50 56,32"/><polyline points="4,58 30,76 56,58"/><polyline points="4,84 30,102 56,84"/>
    </g>
  </svg>
  <svg class="chevrons" style="left:270px;top:272px" width="108" height="58" viewBox="0 0 108 58">
    <g fill="none" stroke="var(--lavender)" stroke-width="8">
      <polyline points="4,4 24,29 4,54"/><polyline points="30,4 50,29 30,54"/><polyline points="56,4 76,29 56,54"/><polyline points="82,4 102,29 82,54"/>
    </g>
  </svg>
  <div class="abs car-photo" role="img" aria-label="Glossy black sports sedan, front three-quarter view"></div>
  <div class="abs call-tag">Call or Text for Appointment</div>
  <div class="abs phone">
    <svg viewBox="0 0 24 24"><path fill="var(--white)" d="M6.6 10.8c1.4 2.8 3.8 5.1 6.6 6.6l2.2-2.2c.3-.3.7-.4 1-.2 1.1.4 2.3.6 3.6.6.6 0 1 .4 1 1V20c0 .6-.4 1-1 1C10.6 21 3 13.4 3 4c0-.6.4-1 1-1h3.5c.6 0 1 .4 1 1 0 1.3.2 2.5.6 3.6.1.3 0 .7-.2 1z"/></svg>
    913-555-0147
  </div>
</section>

</body>
</html>
```